Business cards for education company

We need a business card design for a relatively new company based in Queensland and operating across Australia. We resell diploma level education courses which include Business, Management, Finance, Community Services & Government courses. We offer over 20 different courses.
The target market is for anyone 16 years of age and older. There is no age limit.

We would like to see the design use the color blue and silver. The final design should communicate professionalism and a bright future.

We sell education but are also promoting the career they see themselves in 2-3 years in the future

Our company logo is attached.

Target Market(s)

We target all age groups above 16 years of age. The main target market would be people aged between 17-35.

We focus on those people who cannot make it into University or do not want to commit the time to a full degree.

Industry/Entity Type

Education

Requirements
Must have
• Professional
Company logo
website
Contact details:

Please use the following example:

Lionel Parfitt
Senior Education Consultant
0417 386 591
Lionel.parfitt@brightwaylearninghub.com.au
www.brightwaylearninghub.com.au

```html
<!DOCTYPE html>
<html lang="en">
<head>
<meta charset="utf-8">
<title>Brightway Learning Hub – Business Cards</title>
<link rel="stylesheet" href="https://fonts.googleapis.com/css2?family=Barlow:wght@400;500;700&display=swap">
<style>
  :root {
    --bg: #e9e9ec;
    --card: #ffffff;
    --brand-blue: #1f5fb4;
    --deep-blue: #0e2f7a;
    --bright-blue: #3b7fd6;
    --silver: #5b5e66;
    --ink: #2a2c33;
    --muted: #4a4d55;
  }
  * { margin: 0; padding: 0; box-sizing: border-box; }
  html, body {
    width: 1200px; height: 443px; overflow: hidden;
    background: var(--bg);
    font-family: "Barlow", Arial, sans-serif;
  }
  .stage {
    position: relative; width: 1200px; height: 443px;
    display: flex; justify-content: center; align-items: center; gap: 60px;
  }
  .card {
    position: relative; width: 520px; height: 300px;
    background: var(--card);
    box-shadow: 0 4px 14px rgba(0,0,0,.18);
    overflow: hidden;
  }
  .card__swoosh { position: absolute; inset: 0; width: 100%; height: 100%; }

  .brand { position: absolute; left: 40px; top: 36px; display: flex; align-items: center; gap: 14px; }
  .brand__dot { width: 34px; height: 34px; border-radius: 50%; background: var(--brand-blue); }
  .brand__name {
    font-weight: 700; font-size: 28px; line-height: 1.0; color: var(--brand-blue);
    letter-spacing: .5px; text-transform: uppercase;
  }

  .contact { position: absolute; left: 44px; top: 128px; z-index: 1; }
  .contact__name { font-weight: 700; font-size: 20px; line-height: 1.2; color: var(--brand-blue); letter-spacing: .5px; text-transform: uppercase; }
  .contact__role { font-size: 11px; font-weight: 500; color: var(--muted); letter-spacing: .6px; text-transform: uppercase; margin-top: 2px; }
  .contact__list { list-style: none; margin-top: 12px; }
  .contact__item { display: flex; align-items: center; gap: 7px; font-size: 12.5px; line-height: 16px; font-weight: 500; color: var(--ink); margin-bottom: 5px; }
  .contact__icon { width: 12px; height: 12px; flex: none; }

  .card--back { display: flex; flex-direction: column; align-items: center; justify-content: center; }
  .back__name {
    font-weight: 700; font-size: 50px; line-height: 1.05; text-align: center;
    color: var(--brand-blue); text-transform: uppercase; letter-spacing: 1px;
  }
  .back__web { margin-top: 18px; font-size: 13px; font-weight: 500; color: var(--ink); }
</style>
</head>
<body>
<main class="stage">
  <section class="card card--front" aria-label="Business card front">
    <svg class="card__swoosh" viewBox="0 0 520 300" preserveAspectRatio="none" aria-hidden="true">
      <defs>
        <linearGradient id="bandBlue" x1="0" y1="0" x2="1" y2="0">
          <stop offset="0" stop-color="#ffffff"/>
          <stop offset="0.5" stop-color="#3b7fd6"/>
          <stop offset="1" stop-color="#0e2f7a"/>
        </linearGradient>
      </defs>
      <path d="M0,300 C300,300 460,250 520,110 L520,300 Z" fill="url(#bandBlue)"/>
      <path d="M30,294 C300,292 458,238 520,94" fill="none" stroke="#5b5e66" stroke-width="7"/>
    </svg>

    <div class="brand">
      <span class="brand__dot"></span>
      <span class="brand__name">Brightway<br>Learning Hub</span>
    </div>

    <div class="contact">
      <p class="contact__name">Lionel Parfitt</p>
      <p class="contact__role">Senior Education Consultant</p>
      <ul class="contact__list">
        <li class="contact__item">
          <svg class="contact__icon" viewBox="0 0 16 16" aria-hidden="true"><circle cx="8" cy="8" r="8" fill="#1f5fb4"/><path d="M5.5 4.5c.5-.4 1-.3 1.3.2l.7 1.2c.2.4 0 .8-.3 1l-.4.3c.4.9 1 1.6 1.9 2l.3-.4c.3-.3.7-.4 1-.2l1.2.7c.5.3.5.9.1 1.3-1 1-2.6.8-4.2-.8S4.5 5.5 5.5 4.5z" fill="#fff"/></svg>
          0417 386 591
        </li>
        <li class="contact__item">
          <svg class="contact__icon" viewBox="0 0 16 16" aria-hidden="true"><rect x="1" y="3.5" width="14" height="9" rx="1" fill="#1f5fb4"/><path d="M1.5 4l6.5 5 6.5-5" fill="none" stroke="#fff" stroke-width="1.2"/></svg>
          Lionel.parfitt@brightwaylearninghub.com.au
        </li>
        <li class="contact__item">
          <svg class="contact__icon" viewBox="0 0 16 16" aria-hidden="true"><circle cx="8" cy="8" r="7" fill="#1f5fb4"/><g fill="none" stroke="#fff" stroke-width=".9"><ellipse cx="8" cy="8" rx="3" ry="7"/><path d="M1 8h14M2.5 4.5h11M2.5 11.5h11"/></g></svg>
          www.brightwaylearninghub.com.au
        </li>
      </ul>
    </div>
  </section>

  <section class="card card--back" aria-label="Business card back">
    <p class="back__name">Brightway<br>Learning Hub</p>
    <p class="back__web">www.brightwaylearninghub.com.au</p>
  </section>
</main>
</body>
</html>
```